Business Card Design

We require a business card design for a law firm, our signature colours are maroon and cream. Our slogan is "From our family to yours", we would like the cards to be professional however feminine at the same time.

Industry/Entity Type

Business

Contact Information for Business Card

Helena Brackett & Associates Lawyers & Conveyancers, Helena Brackett LL.B. Principal Solicitor, 17 Quillon Street, Marrowdale NSW 2190

Logo styles of interest
Emblem Logo
Abstract Logo
Wordmark Logo

```html
<!DOCTYPE html>
<html lang="en">
<head>
<meta charset="utf-8">
<title>Helena Brackett &amp; Associates – Business Card</title>
<link rel="stylesheet" href="https://fonts.googleapis.com/css2?family=Arimo:wght@400;700&display=swap">
<style>
  :root {
    --cream-centre: #fcf8ec;
    --cream-edge: #ece4d1;
    --frame: #8b7c70;
    --ornament-tone: #d9cdbf;
    --emblem: #b48d7e;
    --ink: #111111;
  }
  html, body {
    margin: 0;
    padding: 0;
    overflow: hidden;
    background: var(--cream-edge);
  }
  .card {
    position: relative;
    width: 1200px;
    height: 742px;
    overflow: hidden;
    background: radial-gradient(ellipse at 50% 50%, var(--cream-centre) 45%, var(--cream-edge) 100%);
    font-family: "Arimo", Arial, sans-serif;
    color: var(--ink);
  }
  .frame {
    position: absolute;
    inset: 0;
  }
  .corner-ornament {
    position: absolute;
    width: 150px;
    height: 140px;
    border-radius: 24px;
    background: linear-gradient(135deg, var(--ornament-tone), rgba(217,205,191,0.25));
    opacity: 0.55;
  }
  .corner-ornament.top-left { left: 60px; top: 60px; }
  .corner-ornament.top-right { right: 60px; top: 60px; }
  .corner-ornament.bottom-left { left: 60px; bottom: 60px; }
  .corner-ornament.bottom-right { right: 60px; bottom: 60px; }
  .brand-mark {
    position: absolute;
    left: 0;
    right: 0;
    top: 62px;
    display: flex;
    flex-direction: column;
    align-items: center;
    gap: 16px;
  }
  .brand-dot {
    width: 104px;
    height: 104px;
    border-radius: 50%;
    background: var(--emblem);
  }
  .brand-name {
    margin: 0;
    font-size: 30px;
    font-weight: 400;
    letter-spacing: 1px;
    color: var(--emblem);
  }
  .text-block {
    position: absolute;
    left: 0;
    right: 0;
    text-align: center;
    white-space: nowrap;
    margin: 0;
  }
  .firm-name {
    top: 284px;
    font-size: 47px;
    font-weight: 700;
    letter-spacing: 0.2px;
  }
  .firm-services {
    top: 354px;
    font-size: 32px;
    font-weight: 400;
    letter-spacing: 0.6px;
  }
  .person-name {
    top: 440px;
    font-size: 48px;
    font-weight: 400;
    letter-spacing: 0.8px;
  }
  .person-title {
    top: 507px;
    font-size: 32px;
    font-weight: 400;
    letter-spacing: 0.8px;
  }
  .address {
    top: 563px;
    font-size: 35px;
    font-weight: 400;
    letter-spacing: 1px;
  }
</style>
</head>
<body>
  <div class="card">
    <div class="corner-ornament top-left" role="img" aria-label="Scrolled corner flourish"></div>
    <div class="corner-ornament top-right" role="img" aria-label="Scrolled corner flourish"></div>
    <div class="corner-ornament bottom-left" role="img" aria-label="Scrolled corner flourish"></div>
    <div class="corner-ornament bottom-right" role="img" aria-label="Scrolled corner flourish"></div>

    <svg class="frame" width="1200" height="742" viewBox="0 0 1200 742" aria-hidden="true">
      <path d="M216 80 H984 Q1156 80 1156 205 V537 Q1156 662 984 662 H216 Q44 662 44 537 V205 Q44 80 216 80 Z"
            fill="none" stroke="var(--frame)" stroke-width="3"/>
    </svg>

    <div class="brand-mark">
      <span class="brand-dot" aria-hidden="true"></span>
      <p class="brand-name">Helena Brackett</p>
    </div>

    <h1 class="text-block firm-name">Helena Brackett &amp; Associates</h1>
    <p class="text-block firm-services">Lawyers &amp; Conveyancers</p>
    <p class="text-block person-name">Helena Brackett</p>
    <p class="text-block person-title">LL.B. Principal Solicitor</p>
    <p class="text-block address">17 Quillon Street, Marrowdale NSW 2190</p>
  </div>
</body>
</html>
```